Mondaxe custom business card design

Need a authentic, innovative business card design for a new mobile app business. I am uploading a few screen images from our app for you to view. I would like app design theme to match business card design. I can also send logo images.

```html
<!DOCTYPE html>
<html lang="en">
<head>
<meta charset="utf-8">
<title>Mondaxe business card</title>
<link rel="stylesheet" href="https://fonts.googleapis.com/css2?family=Montserrat:wght@900&family=Source+Sans+3:wght@400;700&display=swap">
<style>
  :root {
    --backdrop: #3b3c3e;
    --paper: #ffffff;
    --ink: #1b1b1b;
    --text-grey: #3a3a3a;
    --muted: #6a6a6a;
    --purple: #5a0a91;
    --purple-deep: #47067a;
  }
  * { margin: 0; padding: 0; box-sizing: border-box; }
  html, body {
    width: 1200px; height: 1000px; overflow: hidden;
    background: var(--backdrop);
  }
  .canvas { position: relative; width: 1200px; height: 1000px; }
  .card {
    position: absolute; left: 250px; width: 700px; height: 400px;
    background: var(--paper); overflow: hidden;
    box-shadow: 0 10px 30px rgba(0,0,0,.35);
  }
  .card--back { top: 70px; }
  .card--front { top: 530px; }

  /* back side */
  .back-brand {
    position: absolute; left: 0; right: 0; top: 120px;
    display: flex; flex-direction: column; align-items: center;
  }
  .brand-dot {
    width: 70px; height: 70px; border-radius: 50%;
    background: var(--purple); margin-bottom: 22px;
  }
  .wordmark {
    font-family: "Montserrat", sans-serif; font-weight: 900;
    color: var(--ink); letter-spacing: -0.5px; line-height: 1;
  }
  .back-brand .wordmark { font-size: 46px; }
  .back-url {
    margin-top: 16px;
    font-family: "Source Sans 3", sans-serif; font-size: 18px;
    letter-spacing: 6px; color: var(--muted);
  }

  /* front side */
  .accent-panel {
    position: absolute; right: 0; top: 0; width: 330px; height: 400px;
    background: linear-gradient(160deg, var(--purple), var(--purple-deep));
  }
  .front-info {
    position: absolute; left: 40px; top: 36px;
    font-family: "Source Sans 3", sans-serif; color: var(--text-grey);
  }
  .front-info .wordmark { font-size: 54px; margin-bottom: 26px; }
  .person-name {
    font-weight: 700; font-size: 25px; color: var(--purple);
    letter-spacing: .5px; line-height: 1.05;
  }
  .person-title { font-size: 17px; letter-spacing: .5px; margin-bottom: 12px; }
  .address { font-size: 17px; line-height: 1.25; margin-bottom: 6px; }
  .contact-list { list-style: none; font-size: 17px; line-height: 1.3; }
  .contact-list li { display: flex; align-items: center; gap: 10px; }
  .contact-list svg { width: 14px; height: 14px; fill: var(--purple); flex: none; }
  .contact-list .plain { padding-left: 24px; }
</style>
</head>
<body>
<main class="canvas">

  <section class="card card--back" aria-label="Card back">
    <div class="back-brand">
      <div class="brand-dot"></div>
      <div class="wordmark">Mondaxe</div>
      <div class="back-url">www.mondaxe.com</div>
    </div>
  </section>

  <section class="card card--front" aria-label="Card front">
    <div class="accent-panel"></div>
    <div class="front-info">
      <div class="wordmark">Mondaxe</div>
      <p class="person-name">LENA MARSH</p>
      <p class="person-title">PRESIDENT</p>
      <p class="address">2217 Harbor View Lane<br>Cedar Falls, IA 50613</p>
      <ul class="contact-list">
        <li><svg viewBox="0 0 16 16"><path d="M3 1h3l1 4-2 1a9 9 0 0 0 5 5l1-2 4 1v3c0 1-1 2-2 2A13 13 0 0 1 1 3c0-1 1-2 2-2z"/></svg>555 0142 7781</li>
        <li><svg viewBox="0 0 16 16"><path d="M4 0h8v16H4zM5 2v10h6V2zm3 11a1 1 0 1 0 0 2 1 1 0 0 0 0-2z"/></svg>555 0198 3364</li>
        <li><svg viewBox="0 0 16 16"><path d="M4 1h7v4h3v10H2V5h2zm1 1v5h5V2zM4 9v2h2V9zm3 0v2h2V9zm3 0v2h2V9z"/></svg>555 0176 2290</li>
        <li><svg viewBox="0 0 16 16"><path d="M0 3h16v10H0zm1 1v.4l7 5 7-5V4z"/></svg>lena@mondaxe.com</li>
        <li><svg viewBox="0 0 16 16"><path d="M8 0a8 8 0 1 0 0 16A8 8 0 0 0 8 0zm0 1.5v13a6.5 6.5 0 0 0 0-13zM1.5 8h13"/></svg>www.mondaxe.com</li>
      </ul>
    </div>
  </section>

</main>
</body>
</html>
```